Company Values Graphic

We are looking for a design of our company values that can be used in a variety of places including our website, mousepads, office posters, business cards, etc.

Notes:
- We'd rather have icons/art than photographs on the poster.... so more like an infographic
- The core value group headings are not required, but can be included if you think grouping the values works for your design
- We have a logo for our software product but that logo is not required
- We don't need/want clever images to accompany each value, but some images are fine
- BrightNest logo attached
- BrightNest colors are attached
- BrightNest logo is Nunito Sans ExtraBold 800
- BrightNest website uses Roboto

Our Values - Who we will work with (and who we will not)
The right set of values are essential to building and maintaining a culture that we all wake up eager to be a part of each day. They are foundational to all hiring and firing decisions. They attract the right people and repel the wrong ones.

BE HELPFUL
Make every person and place better because you are there.
Deliver wow with every interaction.

BE HUMBLE
Listen with every muscle.
Passionately help others first.
Seek first to understand.

BE HONEST
Earn trust every day.
Be open and direct.
Treat everyone with fairness and respect.

BE HUMAN
Celebrate passion and action.
Create an environment where people are authentic.
Hire great people and expect a lot from them

BE COURAGEOUS
Dare mighty things.
Make and honor commitments.
All great things start with a small act of courage applied at the right moment.

```html
<!DOCTYPE html>
<html lang="en">
<head>
<meta charset="utf-8">
<title>BrightNest – Our Values</title>
<link href="https://fonts.googleapis.com/css2?family=Nunito+Sans:wght@400;700;800&display=swap" rel="stylesheet">
<style>
:root{
  --orange:#FF5A00;
  --amber:#FF9A00;
  --red:#F20000;
  --ink:#555555;
  --mist:#E6E6E6;
  --backdrop:#D9D9D9;
  --paper:#FFFFFF;
}
*{margin:0;padding:0;box-sizing:border-box}
html,body{width:1020px;height:1200px;overflow:hidden;background:var(--backdrop)}
.slide{position:absolute;width:498px;height:385px;background:var(--paper);overflow:hidden}
.slide svg{display:block;width:100%;height:100%}
.col-left{left:7px}.col-right{left:515px}
.row-1{top:14px}.row-2{top:408px}.row-3{top:801px}
.heading{font-family:"Nunito Sans",sans-serif;font-weight:800}
.bullets{font-family:"Nunito Sans",sans-serif;font-weight:400;font-size:13px;fill:var(--ink)}
.bullets.on-color{fill:var(--paper)}
.white{fill:var(--paper)}
.ink{fill:var(--ink)}
.orange{fill:var(--orange)}.amber{fill:var(--amber)}.red{fill:var(--red)}
.mid{text-anchor:middle}
.brand-name{font-family:"Nunito Sans",sans-serif;font-weight:800;font-size:44px;fill:var(--orange)}
</style>
</head>
<body>

<!-- Petal fan -->
<section class="slide col-left row-1">
<svg viewBox="0 0 861 665">
  <circle cx="431" cy="195" r="95" fill="var(--mist)"/>
  <g fill="none" stroke-width="7" stroke-linecap="round">
    <path d="M326.7 223 A108 108 0 0 0 354.6 271.4" stroke="var(--orange)"/>
    <path d="M361.6 277.7 A108 108 0 0 0 408.5 300.6" stroke="var(--amber)"/>
    <path d="M417.8 302.2 A108 108 0 0 0 444.2 302.2" stroke="var(--red)" stroke-width="9"/>
    <path d="M453.5 300.6 A108 108 0 0 0 500.4 277.7" stroke="var(--amber)"/>
    <path d="M507.4 271.4 A108 108 0 0 0 535.3 223" stroke="var(--orange)"/>
  </g>
  <text class="heading ink mid" x="431" y="185" font-size="32">OUR</text>
  <text class="heading ink mid" x="431" y="228" font-size="32">VALUES</text>

  <path class="orange" d="M95 205 Q65 210 75 260 L105 350 Q125 400 170 375 L290 290 Q320 260 290 220 Q270 200 240 203 Z"/>
  <path class="orange" transform="translate(862 0) scale(-1 1)" d="M95 205 Q65 210 75 260 L105 350 Q125 400 170 375 L290 290 Q320 260 290 220 Q270 200 240 203 Z"/>
  <path class="amber" d="M170 410 Q150 450 190 480 L270 520 Q310 540 330 490 L365 345 Q375 300 335 295 Q310 295 295 310 Z"/>
  <path class="amber" transform="translate(862 0) scale(-1 1)" d="M170 410 Q150 450 190 480 L270 520 Q310 540 330 490 L365 345 Q375 300 335 295 Q310 295 295 310 Z"/>
  <path class="red" d="M395 355 Q430 315 467 355 L518 520 Q530 565 480 565 L385 565 Q332 565 342 520 Z"/>

  <g role="img" aria-label="Icon: two people helping each other"><circle cx="258" cy="248" r="38" class="white"/><circle cx="258" cy="248" r="18" class="orange"/></g>
  <g role="img" aria-label="Icon: meditating person"><circle cx="324" cy="342" r="38" class="white"/><circle cx="324" cy="342" r="18" class="amber"/></g>
  <g role="img" aria-label="Icon: person with heart"><circle cx="431" cy="378" r="38" class="white"/><circle cx="431" cy="378" r="18" class="red"/></g>
  <g role="img" aria-label="Icon: group with heart"><circle cx="536" cy="342" r="38" class="white"/><circle cx="536" cy="342" r="18" class="amber"/></g>
  <g role="img" aria-label="Icon: raised fist"><circle cx="603" cy="250" r="38" class="white"/><circle cx="603" cy="250" r="18" class="orange"/></g>

  <g class="heading white mid" font-size="24">
    <text x="151" y="270">Be</text><text x="151" y="300">Helpful</text>
    <text x="259" y="414">Be</text><text x="259" y="444">Humble</text>
    <text x="431" y="472">Be</text><text x="431" y="502">Honest</text>
    <text x="603" y="418">Be</text><text x="603" y="448">Human</text>
    <text x="702" y="272">Be</text><text x="702" y="302">Courageous</text>
  </g>
</svg>
</section>

<!-- Zigzag drops -->
<section class="slide col-right row-1">
<svg viewBox="0 0 861 665">
  <text class="heading ink mid" x="430" y="88" font-size="38">OUR VALUES</text>
  <path class="orange" d="M39 275 Q80 198 168 196 Q256 198 296 275 L168 470 Z"/>
  <path class="red" d="M296 275 Q336 198 423 196 Q510 198 550 275 L423 470 Z"/>
  <path class="amber" d="M550 275 Q590 198 678 196 Q765 198 805 275 L678 470 Z"/>
  <path class="amber" d="M296 275 L423 470 Q383 548 296 550 Q208 548 169 470 Z"/>
  <path class="orange" d="M550 275 L677 470 Q637 548 550 550 Q462 548 423 470 Z"/>

  <g fill="var(--paper)" stroke-width="4">
    <g role="img" aria-label="Icon: two people helping each other"><circle cx="169" cy="193" r="38" stroke="var(--orange)"/><circle cx="169" cy="193" r="17" class="orange"/></g>
    <g role="img" aria-label="Icon: person with heart"><circle cx="423" cy="193" r="38" stroke="var(--red)"/><circle cx="423" cy="193" r="17" class="red"/></g>
    <g role="img" aria-label="Icon: raised fist"><circle cx="679" cy="193" r="38" stroke="var(--amber)"/><circle cx="679" cy="193" r="17" class="amber"/></g>
    <g role="img" aria-label="Icon: meditating person"><circle cx="290" cy="555" r="38" stroke="var(--amber)"/><circle cx="290" cy="555" r="17" class="amber"/></g>
    <g role="img" aria-label="Icon: group with heart"><circle cx="550" cy="555" r="38" stroke="var(--orange)"/><circle cx="550" cy="555" r="17" class="orange"/></g>
  </g>

  <g class="heading white mid" font-size="21">
    <text x="169" y="270">BE HELPFUL</text>
    <text x="429" y="270">BE HONEST</text>
    <text x="679" y="270">BE COURAGEOUS</text>
    <text x="294" y="403">BE HUMBLE</text>
    <text x="551" y="403">BE HUMAN</text>
  </g>
  <g class="bullets on-color" font-size="11.5">
    <text x="96" y="294">•</text><text x="111" y="294">Make every person and</text><text x="111" y="307">place better because</text><text x="111" y="320">you are there.</text>
    <text x="96" y="338">•</text><text x="111" y="338">Deliver wow with</text><text x="111" y="351">every interaction.</text>
    <text x="357" y="294">•</text><text x="372" y="294">Earn trust every day.</text>
    <text x="357" y="312">•</text><text x="372" y="312">Be open and direct.</text>
    <text x="357" y="330">•</text><text x="372" y="330">Treat everyone with</text><text x="372" y="343">fairness and respect.</text>
    <text x="615" y="294">•</text><text x="630" y="294">Dare mighty things.</text>
    <text x="615" y="312">•</text><text x="630" y="312">Make and honor</text><text x="630" y="325">commitments.</text>
    <text x="615" y="343">•</text><text x="630" y="343">All great things start</text><text x="630" y="356">with a small act of</text><text x="630" y="369">courage applied at</text><text x="630" y="382">the right moment.</text>
    <text x="221" y="427">•</text><text x="236" y="427">Listen with every muscle.</text>
    <text x="221" y="445">•</text><text x="236" y="445">Passionately help</text><text x="236" y="458">others first.</text>
    <text x="221" y="476">•</text><text x="236" y="476">Seek first to understand.</text>
    <text x="470" y="427">•</text><text x="485" y="427">Celebrate passion and action.</text>
    <text x="470" y="445">•</text><text x="485" y="445">Create an environment where</text><text x="485" y="458">people are authentic.</text>
    <text x="470" y="476">•</text><text x="485" y="476">Hire great people and expect</text><text x="485" y="489">a lot from them</text>
  </g>
</svg>
</section>

<!-- Circle arc -->
<section class="slide col-left row-2">
<svg viewBox="0 0 861 665">
  <g role="img" aria-label="Icon: meditating person"><circle cx="318" cy="350" r="46" class="red"/><circle cx="318" cy="346" r="15" class="white"/></g>
  <g role="img" aria-label="Icon: person with heart"><circle cx="404" cy="313" r="46" class="amber"/><circle cx="404" cy="309" r="15" class="white"/></g>
  <g role="img" aria-label="Icon: group with heart"><circle cx="488" cy="350" r="46" class="orange"/><circle cx="488" cy="346" r="15" class="white"/></g>
  <g role="img" aria-label="Icon: two people helping each other"><circle cx="268" cy="425" r="46" class="orange"/><circle cx="268" cy="421" r="15" class="white"/></g>
  <g role="img" aria-label="Icon: raised fist"><circle cx="545" cy="417" r="46" class="red"/><circle cx="545" cy="413" r="15" class="white"/></g>

  <text class="heading ink mid" x="404" y="420" font-size="34">OUR</text>
  <text class="heading ink mid" x="404" y="464" font-size="34">VALUES</text>

  <text class="heading amber" x="331" y="170" font-size="22">BE HONEST</text>
  <text class="heading red" x="110" y="243" font-size="22">BE HUMBLE</text>
  <text class="heading orange" x="542" y="245" font-size="22">BE HUMAN</text>
  <text class="heading orange" x="64" y="385" font-size="22">BE HELPFUL</text>
  <text class="heading red" x="608" y="386" font-size="22">BE COURAGEOUS</text>

  <g class="bullets">
    <text x="333" y="195">•</text><text x="351" y="195">Earn trust every day.</text>
    <text x="333" y="214">•</text><text x="351" y="214">Be open and direct.</text>
    <text x="333" y="234">•</text><text x="351" y="234">Treat everyone with</text><text x="351" y="248">fairness and respect.</text>
    <text x="111" y="268">•</text><text x="129" y="268">Listen with every muscle.</text>
    <text x="111" y="288">•</text><text x="129" y="288">Passionately help</text><text x="129" y="302">others first.</text>
    <text x="111" y="322">•</text><text x="129" y="322">Seek first to understand.</text>
    <text x="543" y="270">•</text><text x="561" y="270">Celebrate passion and action.</text>
    <text x="543" y="289">•</text><text x="561" y="289">Create an environment where</text><text x="561" y="303">people are authentic.</text>
    <text x="543" y="323">•</text><text x="561" y="323">Hire great people and expect</text><text x="561" y="337">a lot from them.</text>
    <text x="66" y="409">•</text><text x="84" y="409">Make every person</text><text x="84" y="423">and place better</text><text x="84" y="437">because you are there.</text>
    <text x="66" y="457">•</text><text x="84" y="457">Deliver wow with</text><text x="84" y="471">every interaction.</text>
    <text x="610" y="410">•</text><text x="628" y="410">Dare mighty things.</text>
    <text x="610" y="430">•</text><text x="628" y="430">Make and honor commitments.</text>
    <text x="610" y="450">•</text><text x="628" y="450">All great things start with a</text><text x="628" y="464">small act of courage applied at</text><text x="628" y="478">the right moment.</text>
  </g>
</svg>
</section>

<!-- Ring with badges -->
<section class="slide col-right row-2">
<svg viewBox="0 0 861 665">
  <circle cx="419" cy="245" r="155" class="orange" stroke="var(--red)" stroke-width="6"/>
  <circle cx="419" cy="245" r="83" class="white"/>
  <text class="heading ink mid" x="416" y="228" font-size="34">OUR</text>
  <text class="heading ink mid" x="416" y="272" font-size="34">VALUES</text>

  <g role="img" aria-label="Icon: two people helping each other"><circle cx="264" cy="240" r="50" class="amber"/><circle cx="264" cy="240" r="42" class="white"/><circle cx="264" cy="240" r="17" class="orange"/></g>
  <g role="img" aria-label="Icon: raised fist"><circle cx="569" cy="240" r="50" class="amber"/><circle cx="569" cy="240" r="42" class="white"/><circle cx="569" cy="240" r="17" class="orange"/></g>
  <g role="img" aria-label="Icon: meditating person"><circle cx="304" cy="355" r="50" class="amber"/><circle cx="304" cy="355" r="42" class="white"/><circle cx="304" cy="355" r="17" class="orange"/></g>
  <g role="img" aria-label="Icon: group with heart"><circle cx="534" cy="355" r="50" class="amber"/><circle cx="534" cy="355" r="42" class="white"/><circle cx="534" cy="355" r="17" class="orange"/></g>
  <g role="img" aria-label="Icon: person with heart"><circle cx="419" cy="410" r="50" class="amber"/><circle cx="419" cy="410" r="42" class="white"/><circle cx="419" cy="410" r="17" class="orange"/></g>

  <g class="heading ink" font-size="22">
    <text x="36" y="192">BE HUMBLE</text>
    <text x="637" y="192">BE COURAGEOUS</text>
    <text x="102" y="367">BE HELPFUL</text>
    <text x="586" y="413">BE HUMAN</text>
    <text x="344" y="499">BE HONEST</text>
  </g>
  <g class="bullets">
    <text x="37" y="217">•</text><text x="55" y="217">Listen with every muscle.</text>
    <text x="37" y="236">•</text><text x="55" y="236">Passionately help</text><text x="55" y="250">others first.</text>
    <text x="37" y="270">•</text><text x="55" y="270">Seek first to understand.</text>
    <text x="639" y="217">•</text><text x="657" y="217">Dare mighty things.</text>
    <text x="639" y="236">•</text><text x="657" y="236">Make and honor</text><text x="657" y="250">commitments.</text>
    <text x="639" y="270">•</text><text x="657" y="270">All great things start with</text><text x="657" y="284">a small act of courage</text><text x="657" y="298">applied at the right</text><text x="657" y="312">moment.</text>
    <text x="103" y="392">•</text><text x="121" y="392">Make every person</text><text x="121" y="406">and place better</text><text x="121" y="420">because you are there.</text>
    <text x="103" y="440">•</text><text x="121" y="440">Deliver wow with</text><text x="121" y="454">every interaction.</text>
    <text x="587" y="438">•</text><text x="605" y="438">Celebrate passion and action.</text>
    <text x="587" y="458">•</text><text x="605" y="458">Create an environment where</text><text x="605" y="472">people are authentic.</text>
    <text x="587" y="492">•</text><text x="605" y="492">Hire great people and expect</text><text x="605" y="506">a lot from them.</text>
    <text x="345" y="523">•</text><text x="363" y="523">Earn trust every day.</text>
    <text x="345" y="542">•</text><text x="363" y="542">Be open and direct.</text>
    <text x="345" y="562">•</text><text x="363" y="562">Treat everyone with</text><text x="363" y="576">fairness and respect.</text>
  </g>
</svg>
</section>

<!-- Fan wheel -->
<section class="slide col-left row-3">
<svg viewBox="0 0 861 665">
  <path class="orange" d="M415 360 L289.8 568.3 A243 243 0 0 1 172 360 Z"/>
  <path class="amber" d="M415 360 L172 360 A243 243 0 0 1 289.8 151.7 Z"/>
  <path class="red" d="M415 360 L289.8 151.7 A243 243 0 0 1 536.5 149.6 Z"/>
  <path class="orange" d="M415 360 L536.5 149.6 A243 243 0 0 1 658 360 Z"/>
  <path class="amber" d="M415 360 L658 360 A243 243 0 0 1 536.5 570.4 Z"/>
  <circle cx="415" cy="360" r="118" class="red"/>
  <path class="amber" d="M415 360 L356 257.8 A118 118 0 0 1 474 257.8 Z"/>
  <circle cx="415" cy="360" r="92" class="white"/>
  <text class="heading ink mid" x="412" y="340" font-size="34">OUR</text>
  <text class="heading ink mid" x="412" y="384" font-size="34">VALUES</text>

  <g role="img" aria-label="Icon: person with heart"><circle cx="416" cy="252" r="30" class="white" stroke="var(--mist)" stroke-width="3"/><circle cx="416" cy="252" r="12" class="red"/></g>
  <g role="img" aria-label="Icon: meditating person"><circle cx="324" cy="305" r="30" class="white" stroke="var(--mist)" stroke-width="3"/><circle cx="324" cy="305" r="12" class="amber"/></g>
  <g role="img" aria-label="Icon: group with heart"><circle cx="508" cy="305" r="30" class="white" stroke="var(--mist)" stroke-width="3"/><circle cx="508" cy="305" r="12" class="red"/></g>
  <g role="img" aria-label="Icon: two people helping each other"><circle cx="323" cy="412" r="30" class="white" stroke="var(--mist)" stroke-width="3"/><circle cx="323" cy="412" r="12" class="orange"/></g>
  <g role="img" aria-label="Icon: raised fist"><circle cx="508" cy="412" r="30" class="white" stroke="var(--mist)" stroke-width="3"/><circle cx="508" cy="412" r="12" class="amber"/></g>

  <g class="heading white mid" font-size="20">
    <text x="412" y="167">BE</text><text x="412" y="190">HONEST</text>
    <text x="239" y="276">BE</text><text x="239" y="299">HUMBLE</text>
    <text x="584" y="262">BE</text><text x="584" y="285">HUMAN</text>
    <text x="247" y="435">BE</text><text x="247" y="458">HELPFUL</text>
    <text x="564" y="444">BE</text><text x="564" y="467">COURAGEOUS</text>
  </g>
  <g class="bullets">
    <text x="355" y="55">•</text><text x="373" y="55">Earn trust every day.</text>
    <text x="355" y="73">•</text><text x="373" y="73">Be open and direct.</text>
    <text x="355" y="90">•</text><text x="373" y="90">Treat everyone with fairness</text><text x="373" y="103">and respect.</text>
    <text x="42" y="205">•</text><text x="60" y="205">Listen with every</text><text x="60" y="217">muscle.</text>
    <text x="42" y="235">•</text><text x="60" y="235">Passionately help</text><text x="60" y="247">others first.</text>
    <text x="42" y="265">•</text><text x="60" y="265">Seek first to</text><text x="60" y="277">understand.</text>
    <text x="655" y="194">•</text><text x="673" y="194">Celebrate passion</text><text x="673" y="207">and action.</text>
    <text x="655" y="224">•</text><text x="673" y="224">Create an environment</text><text x="673" y="237">where people are authentic.</text>
    <text x="655" y="254">•</text><text x="673" y="254">Hire great people and</text><text x="673" y="267">expect a lot from them.</text>
    <text x="35" y="430">•</text><text x="53" y="430">Make every person</text><text x="53" y="442">and place better</text><text x="53" y="455">because you are</text><text x="53" y="467">there.</text>
    <text x="35" y="485">•</text><text x="53" y="485">Deliver wow with</text><text x="53" y="497">every interaction.</text>
    <text x="665" y="419">•</text><text x="683" y="419">Dare mighty things.</text>
    <text x="665" y="436">•</text><text x="683" y="436">Make and honor</text><text x="683" y="448">commitments.</text>
    <text x="665" y="466">•</text><text x="683" y="466">All great things start with</text><text x="683" y="479">a small act of courage</text><text x="683" y="491">applied at the right</text><text x="683" y="504">moment.</text>
  </g>
</svg>
</section>

<!-- Brand closer -->
<section class="slide col-right row-3">
<svg viewBox="0 0 861 665">
  <text class="brand-name mid" x="430" y="345">BrightNest</text>
</svg>
</section>

</body>
</html>
```